Business Card Redesign

We are looking for a designer to redesign our current business card (attached below). The logo itself will not change but the look and feel of the rest of the card needs to be freshened up. The text on the back of the card is to be changed to:
Strategic Alignment
Leadership and Coaching
Sales Force Development
Sales Talent Acquisition
Emotional Intelligence Facilitation & Certification
Guest speaking

The byline needs to be retained "Authentic relationships... courageous living" along with the logo.

All up we will need business cards laid out for 6 people.

Also, once we receive a design that we are happy with we will need the branding to be continued through onto other documentation such as workbook cover pages, email signatures etc and will negotiate with the successful designer on this future piece of work.

Please review our website for more of an idea of who we are, our style, and what we do. www.brightharbourgroup.com.au and www.heartwiseskills-qm-z.com.au.

Thank you for your interest.

```html
<!DOCTYPE html>
<html lang="en">
<head>
<meta charset="utf-8">
<title>Bright Harbour Group – Business Cards</title>
<link rel="stylesheet" href="https://fonts.googleapis.com/css2?family=Open+Sans:ital,wght@0,400;0,600;0,700;1,400&display=swap">
<style>
  :root {
    --backdrop: #d4e9e0;
    --charcoal: #2a2a2c;
    --paper: #f4f5f6;
    --sky: #5aaadf;
    --navy: #1f3f86;
    --ink: #2e2e30;
    --icon-blue: #3d93d6;
    --white: #ffffff;
  }
  * { box-sizing: border-box; margin: 0; padding: 0; }
  html, body { width: 1200px; height: 900px; overflow: hidden; }
  body {
    background: var(--backdrop);
    font-family: "Open Sans", Arial, sans-serif;
    display: flex;
    align-items: center;
    justify-content: center;
    gap: 56px;
  }
  .card {
    position: relative;
    width: 504px;
    height: 308px;
    border-radius: 22px;
    overflow: hidden;
    background: var(--paper);
    box-shadow: 0 10px 28px rgba(40, 70, 60, 0.18);
  }

  /* ---------- Brand side ---------- */
  .brand-panel {
    position: absolute; left: 0; top: 0; width: 100%; height: 124px;
    background: var(--charcoal);
    display: flex; align-items: center; justify-content: center; gap: 14px;
  }
  .brand-mark {
    width: 22px; height: 22px; border-radius: 50%;
    background: var(--sky);
  }
  .brand-name {
    color: var(--white);
    font-size: 30px; font-weight: 600; letter-spacing: -0.5px;
  }
  .tagline-band {
    position: absolute; left: 0; top: 124px; width: 100%; height: 30px;
    background: var(--sky);
    border-top: 5px solid var(--navy);
    display: flex; align-items: center; padding-left: 26px;
    color: var(--white); font-size: 13px; letter-spacing: 0.2px;
  }
  .services {
    position: absolute; left: 30px; top: 166px;
    list-style: none;
  }
  .services li {
    display: flex; align-items: center; gap: 8px;
    font-size: 12px; line-height: 17px; color: var(--ink);
  }
  .services svg { width: 9px; height: 9px; flex: none; }
  .website {
    position: absolute; left: 30px; top: 276px;
    font-size: 12.5px; font-weight: 700; color: var(--navy);
  }

  /* ---------- Contact side ---------- */
  .identity {
    position: absolute; right: 28px; top: 22px; text-align: right;
  }
  .person-name {
    font-size: 25px; font-weight: 600; color: var(--ink); letter-spacing: -0.3px;
  }
  .person-credentials {
    margin-top: 4px;
    font-size: 11px; font-style: italic; line-height: 14px; color: var(--icon-blue);
  }
  .accent-band {
    position: absolute; left: 0; top: 110px; width: 100%; height: 28px;
    background: var(--sky);
    border-bottom: 5px solid var(--navy);
  }
  .accent-band svg { position: absolute; left: 0; top: 0; width: 100%; height: 23px; }
  .contact-panel {
    position: absolute; left: 0; top: 138px; width: 100%; height: 170px;
    background: var(--charcoal);
    padding: 18px 0 0 36px;
  }
  .contact-list { list-style: none; }
  .contact-list li {
    display: flex; align-items: center; gap: 12px;
    min-height: 34px;
    color: var(--white); font-size: 12px; line-height: 15px;
  }
  .contact-icon {
    width: 22px; height: 22px; border-radius: 50%; flex: none;
    background: var(--icon-blue);
    display: flex; align-items: center; justify-content: center;
  }
  .contact-icon svg { width: 12px; height: 12px; }
</style>
</head>
<body>

  <!-- Brand side -->
  <section class="card card--brand">
    <div class="brand-panel">
      <span class="brand-mark"></span>
      <span class="brand-name">Bright Harbour Group</span>
    </div>
    <div class="tagline-band">Genuine Connections...Confident Growth</div>
    <ul class="services">
      <li><svg viewBox="0 0 10 10"><path d="M2 1 L8 5 L2 9 Z" fill="#3d93d6"/></svg>Strategic Alignment</li>
      <li><svg viewBox="0 0 10 10"><path d="M2 1 L8 5 L2 9 Z" fill="#3d93d6"/></svg>Leadership and Coaching</li>
      <li><svg viewBox="0 0 10 10"><path d="M2 1 L8 5 L2 9 Z" fill="#3d93d6"/></svg>Sales Force Development</li>
      <li><svg viewBox="0 0 10 10"><path d="M2 1 L8 5 L2 9 Z" fill="#3d93d6"/></svg>Sales Talent Acquisition</li>
      <li><svg viewBox="0 0 10 10"><path d="M2 1 L8 5 L2 9 Z" fill="#3d93d6"/></svg>Emotional Intelligence Facilitation &amp; Certification</li>
      <li><svg viewBox="0 0 10 10"><path d="M2 1 L8 5 L2 9 Z" fill="#3d93d6"/></svg>Guest speaking</li>
    </ul>
    <div class="website">www.brightharbourgroup.com.au</div>
  </section>

  <!-- Contact side -->
  <section class="card card--contact">
    <div class="identity">
      <div class="person-name">Daniel R. Whitby</div>
      <div class="person-credentials">Executive Coach, Team Facilitator,<br>Keynote Presenter</div>
    </div>
    <div class="accent-band">
      <svg viewBox="0 0 504 23" preserveAspectRatio="none">
        <line x1="300" y1="12" x2="504" y2="12" stroke="#ffffff" stroke-width="1.5"/>
        <circle cx="420" cy="12" r="4" fill="#ffffff"/>
      </svg>
    </div>
    <div class="contact-panel">
      <ul class="contact-list">
        <li>
          <span class="contact-icon">
            <svg viewBox="0 0 12 12"><path d="M3 1 L5 3.5 L4 4.8 Q5 7 7.2 8 L8.5 7 L11 9 L9.8 10.8 Q5.5 11 2.5 7.5 Q0.8 5 1.2 2.2 Z" fill="#ffffff"/></svg>
          </span>0400 317 264
        </li>
        <li>
          <span class="contact-icon">
            <svg viewBox="0 0 12 12"><rect x="3" y="0.8" width="6" height="10.4" rx="1" fill="#ffffff"/><rect x="4" y="2" width="4" height="6.5" fill="#3d93d6"/></svg>
          </span>+613 9000 4821
        </li>
        <li>
          <span class="contact-icon">
            <svg viewBox="0 0 12 12"><rect x="1" y="2.5" width="10" height="7" fill="#ffffff"/><path d="M1 2.5 L6 6.5 L11 2.5" fill="none" stroke="#3d93d6" stroke-width="1"/></svg>
          </span>daniel@brightharbourgroup.com.au
        </li>
        <li>
          <span class="contact-icon">
            <svg viewBox="0 0 12 12"><path d="M6 1 L11 5.5 L9.5 5.5 L9.5 11 L2.5 11 L2.5 5.5 L1 5.5 Z" fill="#ffffff"/><rect x="5" y="7.5" width="2" height="3.5" fill="#3d93d6"/></svg>
          </span>Suite 2.04, 150 Harbour Rd<br>Seaford, Australia 3198
        </li>
      </ul>
    </div>
  </section>

</body>
</html>
```